Business card design needed for a security services business.

We provide a wide range of security services from guard personnel to electronic systems.

Industry/Entity Type

Security Industry

Contact Information for Business Card

Brent Holloway, Owner Office: 780.555.0148; Cell: 780.555.0193 Email: brent@korvanshieldgroup.example; Address 20417 163 St Edmonton, AB T5X 2K8

Colors
0054AA
0677BA
7BADD7
CADEEF
E8F1F8

Requirements
Nice to have
• On the back of the card I would like to possible list the services I provide: Guards Mobiles Live Video Surveillance Access Intrusion

```html
<!DOCTYPE html>
<html lang="en">
<head>
<meta charset="utf-8">
<title>Korvan Shield Group — Business Card</title>
<link rel="stylesheet" href="https://fonts.googleapis.com/css2?family=Lato:wght@400;700;900&display=swap">
<style>
  :root {
    --brand-blue: #0a72be;
    --white: #ffffff;
    --grey: #6d6e71;
    --page: #e9edf1;
  }
  * { margin: 0; padding: 0; box-sizing: border-box; }
  html, body { width: 1200px; height: 992px; overflow: hidden; }
  body {
    background: var(--page);
    font-family: "Lato", sans-serif;
    position: relative;
  }
  .card {
    position: absolute;
    left: 240px;
    width: 720px;
    height: 412px;
    border-radius: 26px;
    overflow: hidden;
    box-shadow: 0 6px 18px rgba(0,0,0,0.15);
  }
  .card--back { top: 50px; background: var(--brand-blue); color: var(--white); }
  .card--front { top: 520px; background: var(--brand-blue); }

  /* back */
  .back-wordmark {
    position: absolute; left: 70px; top: 150px; width: 300px;
    font-weight: 900; font-size: 40px; line-height: 1.05; letter-spacing: 1px;
    color: var(--white);
  }
  .divider { position: absolute; width: 2px; background: currentColor; }
  .card--back .divider { left: 400px; top: 120px; height: 172px; opacity: .9; }
  .services {
    position: absolute; left: 430px; top: 128px; list-style: none;
    font-size: 17px; line-height: 27px; letter-spacing: .3px;
  }
  .services li::before { content: "•"; margin-right: 8px; }

  /* front */
  .front-panel { position: absolute; inset: 0; }
  .front-wordmark {
    position: absolute; left: 0; right: 0; top: 70px; text-align: center;
    font-weight: 900; font-size: 40px; letter-spacing: 2px; color: var(--brand-blue);
  }
  .front-wordmark .mark-square {
    display: inline-block; width: 22px; height: 22px; background: var(--brand-blue);
    margin-right: 14px; vertical-align: 2px;
  }
  .person {
    position: absolute; left: 30px; top: 240px; width: 330px; text-align: right;
    color: var(--white);
  }
  .person__name { font-weight: 900; font-size: 34px; letter-spacing: .5px; text-transform: uppercase; }
  .person__role { font-size: 22px; margin-top: 2px; }
  .card--front .divider { left: 385px; top: 250px; height: 130px; color: var(--white); }
  .contact {
    position: absolute; left: 408px; top: 242px; list-style: none; color: var(--white);
    font-size: 16px; line-height: 25px;
  }
  .contact li { display: flex; align-items: flex-start; gap: 10px; }
  .contact svg { width: 14px; height: 14px; margin-top: 5px; flex: none; }
  .contact .address { line-height: 21px; margin-top: 2px; }
</style>
</head>
<body>

<section class="card card--back" aria-label="Card back">
  <div class="back-wordmark">KORVAN<br>SHIELD<br>GROUP</div>
  <span class="divider"></span>
  <ul class="services">
    <li>Video Surveillance Systems</li>
    <li>Card Access Systems</li>
    <li>Remote Video Monitoring</li>
    <li>Incident &amp; Alarm Response</li>
    <li>Security Guard Personnel</li>
    <li>Mobile Patrols</li>
  </ul>
</section>

<section class="card card--front" aria-label="Card front">
  <svg class="front-panel" viewBox="0 0 720 412" preserveAspectRatio="none" aria-hidden="true">
    <path fill="#ffffff" d="M0,0 H720 V330 C720,300 700,272 660,265 L70,205 C30,200 0,185 0,150 Z"/>
  </svg>
  <div class="front-wordmark"><span class="mark-square"></span>KORVAN SHIELD GROUP</div>

  <div class="person">
    <div class="person__name">Brent Holloway</div>
    <div class="person__role">Owner</div>
  </div>
  <span class="divider"></span>
  <ul class="contact">
    <li><svg viewBox="0 0 16 16"><path fill="#fff" d="M3 1l3 3-2 2c1 2 3 4 5 5l2-2 3 3-2 3C6 15 1 10 1 3z"/></svg>780.555.0148</li>
    <li><svg viewBox="0 0 16 16"><rect x="4" y="1" width="8" height="14" rx="1.5" fill="none" stroke="#fff" stroke-width="1.6"/><circle cx="8" cy="12.5" r="1" fill="#fff"/></svg>780.555.0193</li>
    <li><svg viewBox="0 0 16 16"><rect x="1" y="3" width="14" height="10" fill="#fff"/><path d="M1 3l7 6 7-6" fill="none" stroke="#0a72be" stroke-width="1.4"/></svg>brent@korvanshieldgroup.example</li>
    <li><svg viewBox="0 0 16 16"><circle cx="8" cy="8" r="6.5" fill="none" stroke="#fff" stroke-width="1.5"/><path d="M1.5 8h13M8 1.5c-3 3-3 10 0 13M8 1.5c3 3 3 10 0 13" fill="none" stroke="#fff" stroke-width="1.2"/></svg>www.korvanshieldgroup.example</li>
    <li><svg viewBox="0 0 16 16"><path fill="#fff" d="M8 1a5 5 0 0 0-5 5c0 4 5 9 5 9s5-5 5-9a5 5 0 0 0-5-5zm0 7a2 2 0 1 1 0-4 2 2 0 0 1 0 4z"/></svg><span class="address">20417 163 St Edmonton<br>AB T5X 2K8</span></li>
  </ul>
</section>

</body>
</html>
```